Business Card Design Project

We need a Business Card for an Mechanical Engineering firm in Singapore. The design should be Modern & Technical looking, yet eye catching.

Our company deals in Cutting Tools & Machine Accessories for the Manufacturing Industries such as Oil & Gas, Aero Space, etc... For more information on our Company, you can either email me or view our website www.valtrion.com.sg.

We are trying to revamp our image to give our consumers a fresh new perspective to our company, so we welcome all ideas.

Industry/Entity Type

Business

Requirements
Must have
• Must incorporate New Company Logo into the card as shown in Uploaded file.

```html
<!DOCTYPE html>
<html lang="en">
<head>
<meta charset="utf-8">
<title>Valtrion Tools – Business Card</title>
<link href="https://fonts.googleapis.com/css2?family=Arimo:wght@400;700&display=swap" rel="stylesheet">
<style>
  :root {
    --crimson: #9b1a37;
    --crimson-soft: #d9a5ae;
    --card: #ecebea;
    --ink: #1c1c1c;
    --muted: #3a3a3a;
    --rule: #d3d1cf;
    --backdrop: #dcdad6;
    --icon: #8c8c8c;
  }
  html, body {
    margin: 0;
    width: 1200px;
    height: 900px;
    overflow: hidden;
    background: var(--backdrop);
    font-family: "Arimo", Arial, sans-serif;
  }
  .sheet {
    width: 1200px;
    height: 900px;
    display: flex;
    align-items: center;
    justify-content: center;
    gap: 40px;
  }
  .card {
    position: relative;
    width: 540px;
    height: 309px;
    background: var(--card);
    box-shadow: 0 6px 18px rgba(0,0,0,0.18);
    overflow: hidden;
  }
  .card-lines {
    position: absolute;
    inset: 0;
  }
  .bottom-band {
    position: absolute;
    left: 0; right: 0; bottom: 0;
    height: 38px;
    background: var(--crimson);
  }
  .brand {
    position: absolute;
    display: flex;
    align-items: center;
    gap: 10px;
    color: var(--crimson);
    font-weight: 700;
    font-size: 28px;
    line-height: 34px;
    letter-spacing: 0.5px;
    white-space: nowrap;
  }
  .brand-dot {
    width: 20px;
    height: 20px;
    border-radius: 50%;
    background: var(--crimson);
  }
  .front .brand { left: 290px; top: 104px; }
  .back .brand { left: 190px; top: 92px; }
  .back-website {
    position: absolute;
    left: 212px;
    top: 142px;
    color: var(--crimson);
    font-size: 15px;
  }
  .holder-name {
    position: absolute;
    left: 86px;
    top: 52px;
    font-size: 22px;
    font-weight: 700;
    color: var(--ink);
  }
  .contact-group {
    position: absolute;
    left: 30px;
    border-top: 1px solid var(--rule);
    padding-top: 6px;
  }
  .contact-group.direct { top: 84px; left: 58px; width: 188px; }
  .contact-group.office { top: 180px; width: 330px; }
  .contact-row {
    display: flex;
    align-items: flex-start;
    gap: 8px;
    font-size: 11.5px;
    line-height: 15px;
    color: var(--muted);
    white-space: nowrap;
  }
  .contact-row strong { color: var(--ink); }
  .contact-icon {
    flex: none;
    width: 11px;
    height: 11px;
    margin-top: 2px;
    border-radius: 50%;
    background: var(--icon);
  }
  .spacer-icon { visibility: hidden; }
</style>
</head>
<body>
<main class="sheet">

  <section class="card front" aria-label="Card front">
    <svg class="card-lines" width="540" height="309" viewBox="0 0 540 309" aria-hidden="true">
      <path d="M0 34 H228 Q262 34 262 68 V134 Q262 168 296 168 H540" fill="none" stroke="var(--crimson)" stroke-width="7"/>
      <path d="M40 34 H84" stroke="var(--crimson-soft)" stroke-width="7"/>
      <path d="M410 168 H462" stroke="var(--crimson-soft)" stroke-width="7"/>
    </svg>

    <div class="holder-name">Marissa</div>

    <div class="contact-group direct">
      <div class="contact-row"><span class="contact-icon"></span>Tel: 65-61234567</div>
      <div class="contact-row"><span class="contact-icon"></span>Fax: 65-61234568</div>
      <div class="contact-row"><span class="contact-icon"></span>Email: hello@valtrion.com.sg</div>
    </div>

    <div class="contact-group office">
      <div class="contact-row"><span class="contact-icon"></span><strong>Valtrion Tools Pte Ltd</strong></div>
      <div class="contact-row"><span class="contact-icon spacer-icon"></span>27 Kallang Way #03-12, Meridian Business Hub,</div>
      <div class="contact-row"><span class="contact-icon spacer-icon"></span>Singapore 349278</div>
      <div class="contact-row"><span class="contact-icon"></span>Website: www.valtrion.com.sg</div>
    </div>

    <div class="brand"><span>Valtrion Tools</span><span class="brand-dot"></span></div>

    <div class="bottom-band"></div>
  </section>

  <section class="card back" aria-label="Card back">
    <svg class="card-lines" width="540" height="309" viewBox="0 0 540 309" aria-hidden="true">
      <path d="M0 226 H540" stroke="var(--crimson)" stroke-width="7"/>
      <path d="M82 226 H136" stroke="var(--crimson-soft)" stroke-width="7"/>
    </svg>

    <div class="brand"><span>Valtrion Tools</span><span class="brand-dot"></span></div>
    <div class="back-website">Website: www.valtrion.com.sg</div>
  </section>

</main>
</body>
</html>
```